Business Card Design

We need a business card design for an existing business. Our main trading brand is www.brightmeadowsaver.co.uk

We attach various logo files - please use the version that will produce the sharpest image on the business card.

We are flexible about shape of card etc. Please think outside the box as to what goes on front and what goes on back of the card

We want to be able to amend the card (once the design has been agreed ) to add additional staff details, but the text to go on it will be generic

Details to go on card ( for the first generic one) are fairly minimal as we don't like cluttered business cards:-

Tom Harker
Managing Director

Mobile: 07812 548 207
Email: t.harker@brightmeadowsaver.co.uk

```html
<!DOCTYPE html>
<html lang="en">
<head>
<meta charset="utf-8">
<title>Bright Meadow Saver – Business Card</title>
<link rel="stylesheet" href="https://fonts.googleapis.com/css2?family=Didact+Gothic&family=Open+Sans:wght@400;600;700&display=swap">
<style>
  :root {
    --stage: #e9e7e3;
    --card: #ffffff;
    --card-shade: #eef0f2;
    --ice: #5bb4e5;
    --ice-soft: #9fd3f0;
    --navy: #2f5b85;
    --navy-deep: #27496b;
    --ink: #3c4650;
    --band-sub: #dcecf8;
  }
  * { box-sizing: border-box; margin: 0; padding: 0; }
  html, body { width: 1057px; height: 1200px; overflow: hidden; }
  body {
    background: var(--stage);
    font-family: "Open Sans", Arial, sans-serif;
    position: relative;
  }
  .card {
    position: absolute;
    left: 98px;
    width: 860px;
    height: 491px;
    background: radial-gradient(ellipse at 45% 40%, var(--card) 55%, var(--card-shade) 100%);
    box-shadow: 0 6px 22px rgba(0,0,0,0.18);
    overflow: hidden;
  }
  .card--front { top: 60px; }
  .card--back { top: 648px; }

  .brand {
    display: flex;
    align-items: center;
    gap: 14px;
    font-family: "Didact Gothic", "Century Gothic", sans-serif;
    color: var(--ice);
    letter-spacing: 0.5px;
    white-space: nowrap;
  }
  .brand__dot {
    border-radius: 50%;
    background: var(--ice-soft);
    flex: none;
  }
  .card--front .brand {
    position: absolute;
    left: 50%; top: 50%;
    transform: translate(-50%, -50%);
    font-size: 44px;
  }
  .card--front .brand__dot { width: 34px; height: 34px; }

  .card--back .brand {
    position: absolute;
    left: 58px; top: 196px;
    font-size: 30px;
  }
  .card--back .brand__dot { width: 24px; height: 24px; }

  .name-band {
    position: absolute;
    right: 0; top: 44px;
    width: 372px; height: 104px;
    background: var(--navy);
    border-left: 10px solid var(--ice);
    color: #fff;
    display: flex;
    flex-direction: column;
    justify-content: center;
    align-items: center;
    text-transform: uppercase;
    white-space: nowrap;
  }
  .name-band__name { font-size: 30px; font-weight: 600; letter-spacing: 2px; }
  .name-band__role { font-size: 15px; letter-spacing: 3px; margin-top: 4px; color: var(--band-sub); }

  .contacts {
    position: absolute;
    left: 62px; top: 296px;
    list-style: none;
  }
  .contacts__item {
    display: flex;
    align-items: center;
    gap: 14px;
    height: 40px;
    font-size: 15px;
    color: var(--ink);
    white-space: nowrap;
  }
  .contacts__icon {
    width: 24px; height: 24px;
    background: var(--navy-deep);
    display: flex; align-items: center; justify-content: center;
    flex: none;
  }
  .contacts__icon svg { width: 14px; height: 14px; fill: none; stroke: #fff; stroke-width: 2; stroke-linecap: round; stroke-linejoin: round; }
</style>
</head>
<body>
  <section class="card card--front" aria-label="Card front">
    <div class="brand"><span class="brand__dot"></span><span class="brand__name">brightmeadowsaver.co.uk</span></div>
  </section>

  <section class="card card--back" aria-label="Card back">
    <div class="name-band">
      <span class="name-band__name">Tom Harker</span>
      <span class="name-band__role">Managing Director</span>
    </div>

    <div class="brand"><span class="brand__dot"></span><span class="brand__name">brightmeadowsaver.co.uk</span></div>

    <ul class="contacts">
      <li class="contacts__item">
        <span class="contacts__icon"><svg viewBox="0 0 24 24"><rect x="6" y="2" width="12" height="20" rx="2"/><path d="M11 18h2"/></svg></span>
        07812 548 207
      </li>
      <li class="contacts__item">
        <span class="contacts__icon"><svg viewBox="0 0 24 24"><rect x="3" y="5" width="18" height="14" rx="1"/><path d="M3 6l9 7 9-7"/></svg></span>
        t.harker@brightmeadowsaver.co.uk
      </li>
    </ul>
  </section>
</body>
</html>
```